I need a book cover design for my book "Scarlet Brambles." It is a non-fiction book focused on answering the question of whether American evangelicals look more like the Pharisees than Jesus.

The subtitle is "The Quiet Parallels of Modern Suburban Townsfolk and an Ancient Kingdom's Proud Rulers." The author name is Colin Marwood.

I will be publishing this as an ebook and paperback.

I am open to all ideas, but will share the only thought I had as a possible design. In the title, the third letter in both words is "A." I thought about the idea of having the "A" in "Evangelical" have a halo and the "A" in "Pharisees" somehow seem to be a shadow of that first "A" but have devil horns instead of a halo. Again, I'm not sold on that, but am sharing it as one design possibility.

I am not interested in the book cover design having a cheesy religious look to it (as many do). I am more interested in it looking like a professional non-fiction cover.

```html
<!DOCTYPE html>
<html lang="en">
<head>
<meta charset="utf-8">
<title>Scarlet Brambles — Cover Concepts</title>
<link rel="stylesheet" href="https://fonts.googleapis.com/css2?family=Great+Vibes&family=Josefin+Sans:wght@400;600&display=swap">
<style>
  :root {
    --paper: #ffffff;
    --canvas: #ffffff;
    --frame: #3a3a3a;
    --scarlet: #be1e2d;
    --ash: #d1d2d4;
    --ink: #000000;
  }
  * { box-sizing: border-box; margin: 0; padding: 0; }
  html, body {
    width: 1200px;
    height: 910px;
    overflow: hidden;
    background: var(--canvas);
  }
  .sheet {
    position: relative;
    width: 1200px;
    height: 910px;
  }
  .cover {
    position: absolute;
    top: 29px;
    width: 474px;
    height: 861px;
    background: var(--paper);
    border: 1px solid var(--frame);
    overflow: hidden;
  }
  .cover--front { left: 123px; }
  .cover--alt   { left: 611px; }

  .cover__artwork {
    position: absolute;
    left: 0;
    right: 0;
    bottom: 0;
    background: linear-gradient(90deg, var(--ash) 0%, var(--scarlet) 55%, var(--ink) 100%);
    opacity: 0.85;
  }
  .cover--front .cover__artwork { top: 308px; }
  .cover--alt .cover__artwork   { top: 0; }

  .cover__title {
    position: absolute;
    top: 36px;
    left: 0;
    right: 0;
    text-align: center;
    font-family: "Great Vibes", cursive;
    font-weight: 400;
    font-size: 62px;
    line-height: 1;
    color: var(--scarlet);
    white-space: nowrap;
  }
  .cover__rule {
    position: absolute;
    left: 67px;
    width: 338px;
    height: 3px;
    background: var(--scarlet);
  }
  .cover__rule--top    { top: 118px; }
  .cover__rule--bottom { top: 184px; }

  .cover__subtitle {
    position: absolute;
    top: 134px;
    left: 0;
    right: 0;
    text-align: center;
    font-family: "Josefin Sans", sans-serif;
    font-weight: 600;
    font-size: 13px;
    line-height: 18px;
    text-transform: uppercase;
    color: var(--ink);
  }
  .cover__author {
    position: absolute;
    top: 200px;
    left: 0;
    right: 0;
    text-align: center;
    font-family: "Josefin Sans", sans-serif;
    font-weight: 600;
    font-size: 34px;
    line-height: 1;
    text-transform: uppercase;
    color: var(--scarlet);
  }
</style>
</head>
<body>
<main class="sheet">

  <section class="cover cover--front">
    <div class="cover__artwork" role="img" aria-label="Cover artwork: three overlapping crosses in grey, red and black"></div>
    <h1 class="cover__title">Scarlet Brambles</h1>
    <div class="cover__rule cover__rule--top"></div>
    <p class="cover__subtitle">The Quiet Parallels of Modern Suburban Townsfolk<br>and an Ancient Kingdom’s Proud Rulers</p>
    <div class="cover__rule cover__rule--bottom"></div>
    <p class="cover__author">Colin Marwood</p>
  </section>

  <section class="cover cover--alt">
    <div class="cover__artwork" role="img" aria-label="Back cover artwork: enlarged overlapping crosses in grey, red and black"></div>
  </section>

</main>
</body>
</html>
```